Marlow Vale Brewery website design,

I would like a website designed for my microbrewery, with a part that you can purchase beers from, links to our social media. The brand is luxury, old English, classic, timeless, simple, crisp and clean. I’d like to send you a design we have for the beer can so you can get understanding of what we are trying to achieve.

Please have a look at our Instagram and Facebook to get an understanding of what we are about.

Thank you.

Ned

Target Market(s)

Non beardy beer drinkers. Young, professional, seeking experiences and something to remember.

Industry/Entity Type

Brewery

Font styles to use
Other font styles liked:
• I will upload photos of what I’d like.

Colors

Designer to choose colors to be used in the design.

Requirements
Must have
• Photos of our beers, it must be a beautiful website, landing page video background of a beer slowly being poured into a glass.
Nice to have
• Shots of hops, grain, videos of steam from the brewing process.

```html
<!DOCTYPE html>
<html lang="en">
<head>
<meta charset="utf-8">
<title>Marlow Vale Brewery</title>
<link href="https://fonts.googleapis.com/css2?family=Lato:ital,wght@0,400;0,700;0,900;1,900&family=Libre+Baskerville&display=swap" rel="stylesheet">
<style>
  :root {
    --gold: #b78a4e;
    --gold-light: #c9a063;
    --bg-dark: #221d1e;
    --bg-header: #1c1819;
    --bg-partners: #1b1718;
    --bg-footer: #141112;
    --text-light: #f2eeea;
    --text-muted: #8a8586;
  }
  * { margin: 0; padding: 0; box-sizing: border-box; }
  html, body { width: 781px; height: 1200px; overflow: hidden; background: var(--bg-dark); }
  body { font-family: "Lato", sans-serif; color: var(--text-light); position: relative; }

  .site-header {
    position: absolute; top: 0; left: 0; width: 781px; height: 83px;
    background: var(--bg-header); z-index: 3;
  }
  .brand {
    position: absolute; left: 50px; top: 24px; display: flex; align-items: center; gap: 10px;
    font-family: "Libre Baskerville", serif; color: var(--gold); font-size: 14px;
    letter-spacing: 2px; text-transform: uppercase;
  }
  .brand-mark { width: 30px; height: 30px; border: 2px solid var(--gold); }
  .main-nav { position: absolute; top: 41px; left: 0; width: 781px; }
  .main-nav a {
    position: absolute; transform: translateX(-50%);
    font-family: "Libre Baskerville", serif; font-size: 8.5px; color: var(--text-light);
    text-decoration: none; text-transform: uppercase; letter-spacing: .3px; white-space: nowrap;
  }
  .main-nav a.active { color: var(--gold); font-weight: 700; }

  .hero {
    position: absolute; top: 83px; left: 0; width: 781px; height: 359px;
    background: linear-gradient(100deg, #3a2a24 0%, #5a4034 30%, #2e2624 55%, #4d4642 75%, #2a2424 100%);
  }
  .hero-title {
    position: absolute; left: 49px; top: 106px; font-weight: 900; font-style: italic;
    font-size: 50px; line-height: 43px; color: #fff; text-transform: uppercase; letter-spacing: -.5px;
  }
  .play-video {
    position: absolute; left: 50px; top: 202px; display: flex; align-items: center; gap: 10px;
    font-weight: 700; font-size: 14px; color: #fff; text-decoration: underline; text-underline-offset: 3px;
  }

  .feature-cards { position: absolute; top: 408px; left: 0; width: 781px; height: 166px; z-index: 2; }
  .feature-card {
    position: absolute; top: 0; width: 216px; height: 166px; border: 2px solid var(--gold);
    display: flex; align-items: center; justify-content: center;
    font-weight: 700; font-size: 27px; color: #fff; text-transform: uppercase;
  }
  .card-about { left: 50px; background: linear-gradient(135deg, #5a4230, #2f2622 60%, #6a4e34); }
  .card-beers { left: 282px; background: linear-gradient(135deg, #3e4450, #2a2c34 55%, #4a3a2c); }
  .card-stockists { left: 516px; background: linear-gradient(135deg, #5a4638, #3a3640 55%, #6a4a38); }

  .welcome { position: absolute; top: 626px; left: 48px; width: 400px; }
  .welcome h1 {
    color: var(--gold); font-size: 22px; line-height: 25px; font-weight: 700; text-transform: uppercase;
  }
  .welcome p { font-size: 10.5px; line-height: 18px; margin-top: 20px; }
  .welcome p + p { margin-top: 30px; }
  .btn-read-more {
    position: absolute; left: 40px; top: 873px; width: 99px; height: 33px; background: var(--gold);
    color: #fff; font-size: 10px; font-weight: 700; text-transform: uppercase;
    display: flex; align-items: center; justify-content: center;
  }
  .product-can {
    position: absolute; left: 498px; top: 600px; width: 153px; height: 290px; border-radius: 26px;
    background: linear-gradient(90deg, #0c0c0c, #2a2a2a 35%, #0e0e0e 70%, #1a1a1a);
    border-top: 12px solid #a88a4a;
  }

  .partners {
    position: absolute; top: 970px; left: 0; width: 781px; height: 106px; background: var(--bg-partners);
  }
  .partner {
    position: absolute; top: 44px; transform: translateX(-50%); font-weight: 900; font-size: 17px;
    color: var(--text-muted); white-space: nowrap; display: flex; align-items: center; gap: 6px;
  }
  .partner .dot { width: 14px; height: 14px; border-radius: 50%; background: var(--text-muted); }

  .site-footer {
    position: absolute; top: 1076px; left: 0; width: 781px; height: 124px; background: var(--bg-footer);
    text-align: center;
  }
  .footer-nav { margin-top: 37px; display: flex; justify-content: center; gap: 26px; }
  .footer-nav a { color: #fff; text-decoration: none; font-size: 9.5px; font-weight: 700; text-transform: uppercase; }
  .copyright { font-size: 7.5px; margin-top: 12px; color: #ddd; }
  .social { display: flex; justify-content: center; gap: 14px; margin-top: 10px; }
  .social span { width: 11px; height: 11px; border-radius: 50%; background: #fff; display: block; }
</style>
</head>
<body>
  <header class="site-header">
    <div class="brand"><span class="brand-mark"></span>Marlow Vale Brewery</div>
    <nav class="main-nav">
      <a class="active" style="left:377px">Home</a>
      <a style="left:443px">About us</a>
      <a style="left:517px">Services</a>
      <a style="left:582px">Sales</a>
      <a style="left:631px">Blog</a>
      <a style="left:702px">Contact us</a>
    </nav>
  </header>

  <section class="hero" role="img" aria-label="Beer being poured from a chrome tap into a glass">
    <h2 class="hero-title">Marlow Vale<br>Brewery</h2>
    <div class="play-video">
      <svg width="34" height="34" viewBox="0 0 34 34"><circle cx="17" cy="17" r="17" fill="#fff"/><path d="M13 10 L25 17 L13 24 Z" fill="#2a2424"/></svg>
      Play video
    </div>
  </section>

  <div class="feature-cards">
    <div class="feature-card card-about" role="img" aria-label="Bar beer taps">About us</div>
    <div class="feature-card card-beers" role="img" aria-label="Opener lifting caps from bottles">Our beers</div>
    <div class="feature-card card-stockists" role="img" aria-label="Copper brewhouse interior">Stockists</div>
  </div>

  <section class="welcome">
    <h1>Welcome to<br>Marlow Vale Brewery</h1>
    <p>Aliquam molestie, mi et imperdiet euismod, dui purus auctor tellus,<br>et interdum lacus lectus et ante. Sed accumsan sollicitudin sapien, sit amet adipiscing turpis gravida ac. In congue, neque ac lobortis volutpat, libero mauris varius mi, vitae suscipit ipsum ligula vitae risus.</p>
    <p>Duis aliquam nibh a dui iaculis viverra id a velit. Vivamus egestas risus in magna varius commodo. Sed semper viverra egestas. Etiam pretium porttitor lectus, vel ornare neque porta volutpat.</p>
  </section>
  <div class="btn-read-more">Read more</div>
  <div class="product-can" role="img" aria-label="Black and gold porter beer can"></div>

  <section class="partners">
    <div class="partner" style="left:88px"><span class="dot"></span>Hollin</div>
    <div class="partner" style="left:236px">Tagline Co</div>
    <div class="partner" style="left:384px">Arvex</div>
    <div class="partner" style="left:532px">Fernbrook Society</div>
    <div class="partner" style="left:680px">Wexley</div>
  </section>

  <footer class="site-footer">
    <nav class="footer-nav">
      <a>Home</a><a>About us</a><a>Services</a><a>Blog</a><a>Sales</a><a>Contact us</a>
    </nav>
    <p class="copyright">Copyright © 2018Company Name.&nbsp; All Right Reserved</p>
    <div class="social" aria-label="Social media links">
      <span></span><span></span><span></span><span></span><span></span>
    </div>
  </footer>
</body>
</html>
```